Brochure for a Laundry

We need a Brochure Designed for a the Crestline Laundry (www.thecrestlnielaundry.com)
A SAMPLE BROCHURE by the Owner of the Brand is also attached for complete review. We need something along the same lines.

Please see the DROPBOX Link below to access the complete Content including written content, pictures, Sample Brochure etc
DROPBOX LINK:
https://www.filevaultly.net/sh/pqrtwbnhekuzdla/XKT-BandoPLe7yUWnQsVsO4zk?dl=0

```html
<!DOCTYPE html>
<html lang="en">
<head>
<meta charset="utf-8">
<title>The Crestline Laundry – Brochure Page</title>
<link rel="stylesheet" href="https://fonts.googleapis.com/css2?family=Open+Sans:wght@400&display=swap">
<style>
  :root {
    --page-bg: #2a2627;
    --ink-light: #ffffff;
    --drop-white: #ffffff;
  }
  html, body {
    margin: 0;
    padding: 0;
    width: 1200px;
    height: 1000px;
    overflow: hidden;
    background: var(--page-bg);
  }
  .brochure-page {
    position: relative;
    width: 1200px;
    height: 1000px;
    background: var(--page-bg);
    overflow: hidden;
    font-family: "Open Sans", Arial, sans-serif;
  }
  .page-shapes {
    position: absolute;
    inset: 0;
  }
  .about-copy {
    position: absolute;
    left: 73px;
    top: 191px;
    width: 430px;
    color: var(--ink-light);
    font-size: 16px;
    line-height: 20.6px;
  }
  .about-copy p {
    margin: 0 0 20.6px 0;
  }
</style>
</head>
<body>
<main class="brochure-page">
  <svg class="page-shapes" width="1200" height="1000" viewBox="0 0 1200 1000" xmlns="http://www.w3.org/2000/svg">
    <defs>
      <linearGradient id="workshop-tones" x1="0" y1="0" x2="0" y2="1">
        <stop offset="0" stop-color="#ebe9e8"/>
        <stop offset="0.55" stop-color="#d9d7d6"/>
        <stop offset="0.8" stop-color="#c65a4f"/>
        <stop offset="1" stop-color="#e6e3e1"/>
      </linearGradient>
      <linearGradient id="wardrobe-tones" x1="0" y1="0" x2="1" y2="1">
        <stop offset="0" stop-color="#efeeee"/>
        <stop offset="0.5" stop-color="#5a5656"/>
        <stop offset="1" stop-color="#2c3e66"/>
      </linearGradient>
      <linearGradient id="pressing-tones" x1="0" y1="0" x2="1" y2="1">
        <stop offset="0" stop-color="#f1f1f1"/>
        <stop offset="0.45" stop-color="#c9cfd9"/>
        <stop offset="0.7" stop-color="#4f74bf"/>
        <stop offset="1" stop-color="#b9a088"/>
      </linearGradient>
    </defs>

    <path class="photo-drop photo-drop--workshop" role="img"
          aria-label="Photo: staff in white shirts operating industrial washing machines in the open laundry workshop"
          d="M685.5,137 L771.7,222.5 A122.5,122.5 0 1 1 599.3,222.5 Z"
          fill="url(#workshop-tones)"/>

    <path class="photo-drop photo-drop--wardrobe" role="img"
          aria-label="Photo: staff member inspecting a dark jacket hanging on a garment rail"
          d="M685.5,578 L771.7,663.5 A122.5,122.5 0 1 1 599.3,663.5 Z"
          fill="url(#wardrobe-tones)"/>

    <path class="photo-feature" role="img"
          aria-label="Photo: two staff members pressing shirts and trousers on blue ironing tables"
          d="M1200,30 C1090,130 832,390 828,620 C826,820 985,950 1200,965 Z"
          fill="url(#pressing-tones)"/>

    <g class="drop-trio" fill="var(--drop-white)">
      <path d="M146.5,735 L184.2,772.6 A53.5,53.5 0 1 1 108.8,772.6 Z"/>
      <path d="M275.5,735 L313.2,772.6 A53.5,53.5 0 1 1 237.8,772.6 Z"/>
      <path d="M404.5,735 L442.2,772.6 A53.5,53.5 0 1 1 366.8,772.6 Z"/>
    </g>
  </svg>

  <section class="about-copy">
    <p>The Crestline Laundry is the only laundry services company to have a central workshop, located in the heart of the Harbourview Metropolitan. Our “open laundry” center makes it possible for anyone to view the quality of care that we put into our laundry and dry cleaning services. Customers and clients have the ability to visit the location during operating hours, and see the eight step process that every single garment undergoes. A complete fabric care process has been established and it is used for all garments.</p>
    <p>The location is conveniently located at the Eastgate, and strategically placed as a way of serving high-fashion consumers throughout the city of Marlow Bay and stretching into Harbourview Kestrel and into the Fernhill District.</p>
    <p>If you are in the area, stop in and meet some of our employees. The care we take may just surprise you!</p>
  </section>
</main>
</body>
</html>
```